Lindavo Civic Growth Planning New web site

Design a new web site. I have a budget of $1,500.00.
Attached on PowerPoint is a complete site plan. Home page and linked pages.
10 - 12 pages. All copy and photos will be supplied. (300dpi)
I have shown them the concept which they like.
No data bases required. Home page with animations dissolving.
They former web site has been taken down. They have been in business 30 years in New Jersey
Colors teal blues and greens
There will be a new logo)being designed)
The text in home page copy will give you a detailed story what they are all about.
Updates

files have been approved for Lindavo, Inc.   Teodor is the designer

Industry/Entity Type

Community

```html
<!DOCTYPE html>
<html lang="en">
<head>
<meta charset="utf-8">
<title>Lindavo, Inc.</title>
<link href="https://fonts.googleapis.com/css2?family=Open+Sans:wght@400;600;700&display=swap" rel="stylesheet">
<style>
:root{
  --green:#129a12;
  --green-dark:#0c7f0c;
  --blue:#1a8fe3;
  --blue-link:#1f8fe0;
  --text:#555;
  --heading-green:#128a12;
  --footer:#262626;
  --footer-bottom:#1c1c1c;
  --footer-text:#d8d8d8;
  --line:#ececec;
}
*{box-sizing:border-box;margin:0;padding:0}
html,body{width:1200px;height:2296px;overflow:hidden}
body{position:relative;background:#fff;font-family:"Open Sans",Arial,sans-serif;color:var(--text)}
.abs{position:absolute}
.top-backdrop{left:0;top:0;width:1200px;height:478px;background:linear-gradient(180deg,#e6edf5 0%,#eef3f8 60%,#f6f8fb 100%)}
.brand{left:130px;top:28px;font-size:33px;font-weight:700;color:var(--green);letter-spacing:.5px}
.social-top{left:906px;top:40px;display:flex;gap:6px}
.social-top span{width:22px;height:22px;border-radius:50%;background:#5a6e86;border:2px solid #fff;box-shadow:0 0 0 1px #c9d3de}
.main-nav{left:130px;top:96px;width:938px;height:70px;background:var(--green);display:flex}
.main-nav a{color:#fff;text-decoration:none;font-size:15.5px;line-height:70px;padding:0 27px}
.main-nav a.active{background:var(--green-dark)}
.main-nav a:last-child{margin-left:auto}
.hero{left:130px;top:184px;width:938px;height:487px;background:linear-gradient(160deg,#eef0f0 0%,#dfe2e2 45%,#e7b24a 62%,#c98a5c 78%,#e4e6e6 100%)}
.hero-shadow{left:170px;top:671px;width:858px;height:24px;background:radial-gradient(ellipse at top,rgba(0,0,0,.16),transparent 70%)}
.slider-dots{left:550px;top:618px;width:73px;height:24px;background:var(--blue);border-radius:3px;display:flex;align-items:center;justify-content:center;gap:5px}
.slider-dots i{width:7px;height:7px;border-radius:50%;background:#fff}
.slider-dots i.on{background:#13a013}
.section-title{color:var(--heading-green);font-size:21px;font-weight:400}
.company-title{left:132px;top:738px}
.company-text{left:130px;top:780px;width:515px;font-size:11.5px;line-height:27px;color:#555}
.btn{background:var(--blue);color:#fff;font-size:13px;text-align:center;border-radius:3px}
.view-more{left:130px;top:909px;width:101px;height:31px;line-height:31px}
.company-photo{left:787px;top:751px;width:280px;height:187px;background:linear-gradient(135deg,#dfe6ee,#8fa4bd 55%,#e9ecef)}
.services-title{left:130px;top:986px;display:flex;align-items:center;width:938px}
.services-title::after{content:"";flex:1;height:4px;background:var(--line);margin-left:8px}
.service{top:1042px;width:288px}
.service .pic{height:150px}
.service h3{margin-top:19px;color:var(--blue);font-size:13px;font-weight:700;white-space:nowrap}
.service ul{list-style:none;margin-top:6px;font-size:11.5px;line-height:20px;color:#333}
.map{left:130px;top:1387px;width:938px;height:362px;background:linear-gradient(90deg,#e9e4d8,#efe9dc 40%,#e6e0cc 70%,#cfdbe6)}
.contact-card{left:369px;top:1436px;width:462px;height:286px;background:#fff}
.contact-card h2{position:absolute;top:20px;width:100%;text-align:center;color:var(--heading-green);font-size:19px;font-weight:400}
.contact-row{position:absolute;left:72px;display:flex;gap:18px;font-size:11.5px;line-height:24px;color:#666}
.contact-row svg{flex:none;margin-top:2px}
.contact-social{position:absolute;left:141px;top:237px;display:flex;gap:18px}
.contact-social span{width:16px;height:16px;border-radius:50%;background:#8a8a8a}
.newsletter{left:0;top:1797px;width:1200px;height:112px;background:var(--green)}
.newsletter h2{position:absolute;left:130px;top:28px;color:#fff;font-size:24.5px;font-weight:600}
.newsletter p{position:absolute;left:130px;top:60px;color:#fff;font-size:11px}
.field{top:35px;width:236px;height:43px;background:#fff;border:1px solid #ddd;font-size:11px;color:#999;padding:0 14px;line-height:43px}
.subscribe{left:966px;top:35px;width:102px;height:43px;line-height:43px;font-size:15px;border-radius:0}
.footer{left:0;top:1909px;width:1200px;height:306px;background:var(--footer)}
.footer h4{position:absolute;top:23px;color:#fff;font-size:17.5px;font-weight:400}
.footer .col{position:absolute;top:60px;font-size:13px;line-height:25px;color:var(--footer-text)}
.footer a{color:var(--blue-link);text-decoration:none}
.tweet{position:relative;padding-left:22px;margin-bottom:25px}
.tweet::before{content:"";position:absolute;left:0;top:9px;width:7px;height:6px;background:var(--blue-link);border-radius:50% 50% 50% 0}
.post{display:flex;gap:22px;margin-bottom:12px}
.post .thumb{flex:none;width:50px;height:50px;border:2px solid #eee;background:linear-gradient(135deg,#c23a2a,#e9e2d9 60%,#7a8593)}
.footer-bottom{left:0;top:2215px;width:1200px;height:81px;background:var(--footer-bottom)}
.footer-bottom p{position:absolute;left:130px;top:32px;color:#ddd;font-size:11px}
.footer-social{position:absolute;left:893px;top:32px;display:flex;gap:34px}
.footer-social span{width:16px;height:16px;border-radius:50%;background:var(--green)}
</style>
</head>
<body>
<div class="abs top-backdrop" role="img" aria-label="Faint architectural blueprint drawings as page backdrop"></div>

<div class="abs brand">lindavoinc.org</div>
<div class="abs social-top" aria-label="Social links"><span></span><span></span><span></span><span></span><span></span><span></span></div>

<nav class="abs main-nav">
  <a class="active" href="#">Home</a>
  <a href="#">Our Company</a>
  <a href="#">Services</a>
  <a href="#">Housing Rehab Application</a>
  <a href="#">Affordable Application</a>
  <a href="#">Contact Us</a>
</nav>

<div class="abs hero" role="img" aria-label="Hands drafting a floor plan with a ruler and pencil on blueprints"></div>
<div class="abs hero-shadow"></div>
<div class="abs slider-dots"><i></i><i></i><i class="on"></i><i></i><i></i></div>

<h2 class="abs section-title company-title">OUR COMPANY</h2>
<p class="abs company-text">Lindavo, Inc stands for Community, Grants, Planning and Housing.&nbsp; We specialize in all aspects of affordable housing, planning, COAH compliance, and the procurement of grants and loans for our clients.Founded in 1975, Lindavo has grown to be the only full service affordable housing implementation company in New Jersey.&nbsp; Seasoned in all facets of community d</p>
<div class="abs btn view-more">VIEW MORE</div>
<div class="abs company-photo" role="img" aria-label="Team in hard hats reviewing plans at a table"></div>

<h2 class="abs section-title services-title">SERVICES</h2>

<div class="abs service" style="left:130px">
  <div class="pic" role="img" aria-label="Aerial view of a residential neighborhood" style="background:linear-gradient(135deg,#8c9a6a,#b4b29a 50%,#6f8a5a)"></div>
  <h3>HOUSING AND RELOCATION</h3>
  <ul><li>Relocation</li><li>Housing Development</li><li>Relocation</li><li>COAH Compliance</li><li>Property Acquisition</li></ul>
</div>
<div class="abs service" style="left:456px">
  <div class="pic" role="img" aria-label="Two engineers in hard hats reviewing a drawing" style="background:linear-gradient(135deg,#2a5d9c,#d9dde3 50%,#e38b2e)"></div>
  <h3>COMMUNITY AND ECONOMIC DEVELOPMENT</h3>
  <ul><li>Strategic Planning</li><li>Redevelopment Plans</li><li>CDBG/HOME</li><li>Economic Development</li></ul>
</div>
<div class="abs service" style="left:779px">
  <div class="pic" role="img" aria-label="Blueprint with drafting tools" style="background:linear-gradient(135deg,#cfe3f5,#8fb7df 50%,#e8f1fa)"></div>
  <h3>GRANTS AND FUNDING OPPORTUNITIES</h3>
  <ul><li>Strategic Funding</li><li>Grant Writing</li><li>Our Grants Committee</li><li>Grants Consultant for the New Jersey League</li><li>Public/Private Partnerships</li></ul>
</div>

<div class="abs map" role="img" aria-label="Street map of the office location"></div>
<div class="abs contact-card">
  <h2>CONTACT DETAILS</h2>
  <div class="contact-row" style="top:72px">
    <svg width="18" height="22" viewBox="0 0 18 22"><path d="M9 1a7 7 0 0 0-7 7c0 5 7 13 7 13s7-8 7-13a7 7 0 0 0-7-7z" fill="none" stroke="#1f8fe0" stroke-width="1.6"/><circle cx="9" cy="8" r="2.5" fill="none" stroke="#1f8fe0" stroke-width="1.6"/></svg>
    <div>Harbrine.com<br>48 W. Alder St, Suite 310&nbsp; Dunmore, NJ 08510</div>
  </div>
  <div class="contact-row" style="top:126px">
    <svg width="20" height="20" viewBox="0 0 20 20"><rect x="1" y="1" width="18" height="18" rx="2" fill="none" stroke="#1f8fe0" stroke-width="1.6"/><circle cx="8" cy="8" r="2.5" fill="none" stroke="#1f8fe0" stroke-width="1.4"/><path d="M4 15c1-3 7-3 8 0M13 7h4M13 11h4" stroke="#1f8fe0" stroke-width="1.4" fill="none"/></svg>
    <div>40312958874<br>51829304765</div>
  </div>
  <div class="contact-row" style="top:184px">
    <svg width="22" height="16" viewBox="0 0 22 16"><rect x="1" y="1" width="20" height="14" fill="none" stroke="#1f8fe0" stroke-width="1.6"/><path d="M1 1l10 8 10-8M1 15l7-7M21 15l-7-7" fill="none" stroke="#1f8fe0" stroke-width="1.4"/></svg>
    <div>info@lindavomail.com</div>
  </div>
  <div class="contact-social"><span></span><span></span><span></span><span></span><span></span><span></span></div>
</div>

<section class="abs newsletter">
  <h2>SUBSCRIBE TO NEWSLETTER</h2>
  <p>add stay informed about oue newwa events</p>
  <div class="abs field" style="left:470px">Name</div>
  <div class="abs field" style="left:715px">Mail</div>
  <div class="abs btn subscribe">SUBSCRIBE</div>
</section>

<footer class="abs footer">
  <h4 style="left:130px">About Us</h4>
  <div class="col" style="left:130px;width:270px">Having started operations in 2001, Corvessa Partners is an established “value add” property group<br><br>with a focus on property developmentCorvessa Partners is an<br><a href="#">Read More</a></div>

  <h4 style="left:444px">Latest Tweets</h4>
  <div class="col" style="left:444px;width:250px">
    <div class="tweet">Aenean lacinia bibendum nulla sed leo posuere erat a ante venenatis dapibus <a href="#">Follow @brightkeylab</a></div>
    <div class="tweet">Donec ullamcorper metus auctor fringilla. Nullam <a href="#">Follow @brightkeylab</a></div>
    <div class="tweet"><br><a href="#">Follow @brightkeylab</a>porta</div>
  </div>

  <h4 style="left:779px">Latest Blog posts</h4>
  <div class="col" style="left:777px;width:300px;top:64px">
    <div class="post"><div class="thumb" role="img" aria-label="Blog post thumbnail"></div><div>Vivamus sagittis lacus vel augue leet rutrum dolor auctor.<br><a href="#">2 Days Ago</a></div></div>
    <div class="post"><div class="thumb" role="img" aria-label="Blog post thumbnail" style="background:linear-gradient(135deg,#f2f2f2,#9aa3ad)"></div><div>Scelerisque nisl consectetur et.lorem<br><a href="#">2 Days Ago</a></div></div>
    <div class="post"><div class="thumb" role="img" aria-label="Blog post thumbnail" style="background:linear-gradient(135deg,#6f8fb5,#e2b23a 60%,#c9342a)"></div><div>Pellentesque ornare sem lacinia qua venenatis vestibulum. Fusce<br><a href="#">3 Days Ago</a></div></div>
  </div>
</footer>

<div class="abs footer-bottom">
  <p>©2014&nbsp; All rights reserved.&nbsp;&nbsp; Disclaimer&nbsp;&nbsp; //&nbsp;&nbsp; Contact</p>
  <div class="footer-social"><span></span><span></span><span></span><span></span></div>
</div>
</body>
</html>
```